www.dorvanpipeandboiler.com

I want everything on this page plus I need to add a ad that say save up to 20% on new installation.. also need to add a KTW logo sense I sing up with the KTW in San Diego CA. Just need this page to look more professional.
I had come to realize that I will need to convert the SPD file to HTML in order to upload to my site, so if any one is interested in doing the complete work let me know I know I need to raise my budget which I am working on that already. I had contacted support.
Remember for the header where you guys use picture, I be using my on pictures most likely a slide show of pictures so one design with different picture don't make different because I still will replaced it with my own. at my location in my industry the customer the faster they can see the phone number, the services and company experience the better.
New customers

```html
<!DOCTYPE html>
<html lang="en">
<head>
<meta charset="utf-8">
<title>Dorvan Pipe &amp; Boiler Inc.</title>
<link rel="stylesheet" href="https://fonts.googleapis.com/css2?family=Roboto:ital,wght@0,400;0,500;0,700;1,700&display=swap">
<style>
:root{
  --blue:#0a78c8;
  --blue-dark:#075ea3;
  --red:#8b2a2a;
  --orange:#f39c12;
  --orange-light:#f9c21a;
  --grey:#c9c9c9;
  --grey-line:#e4e4e4;
  --text:#3a3a3a;
  --white:#ffffff;
}
*{box-sizing:border-box;margin:0;padding:0}
html,body{width:944px;height:1200px;overflow:hidden;background:var(--white)}
body{position:relative;font-family:"Roboto",sans-serif;color:var(--text)}
.abs{position:absolute}

/* header */
.brand{left:118px;top:22px;width:130px;color:var(--red);font-weight:700;font-size:13px;line-height:15px;text-transform:uppercase}
.brand .dot{display:inline-block;width:12px;height:12px;border-radius:50%;background:var(--orange);vertical-align:-1px;margin-right:5px}
.emergency{left:539px;top:22px;color:var(--red);font-weight:500;font-size:17px;line-height:24px}
.emergency .num{color:#555}
.follow{font-size:10.5px;color:var(--red);font-weight:500}
.social{display:flex;gap:11px}
.social span{width:21px;height:21px;border-radius:50%;background:#333;display:block}

/* nav */
.nav-lines{left:0;top:92px;width:944px;height:38px;border-top:1px solid var(--red);border-bottom:1px solid var(--red)}
.nav{left:21px;top:93px;width:901px;height:36px;background:var(--blue);display:flex}
.nav a{color:var(--white);text-decoration:none;font-weight:500;font-size:13px;line-height:36px;text-align:center;border-right:1px solid rgba(255,255,255,.35)}
.nav a.active{background:var(--red)}
.nav-call{left:651px;top:93px;width:37px;height:36px;background:var(--orange);display:flex;align-items:center;justify-content:center}
.nav-number{left:699px;top:93px;line-height:36px;color:var(--white);font-weight:700;font-size:18px}

/* hero */
.hero{left:0;top:130px;width:944px;height:370px;background:linear-gradient(100deg,#8f8a86 0%,#b9b6b2 35%,#6e6258 60%,#b9aca0 100%)}
.tagline{left:242px;top:478px;width:460px;height:44px;background:var(--blue);color:var(--white);font-weight:500;font-size:20px;line-height:44px;text-align:center}

/* welcome */
.welcome-title{left:121px;top:584px;display:flex;align-items:center;gap:10px}
.welcome-title h1{font-size:21px;font-style:italic;font-weight:700;color:var(--blue)}
.welcome-title .brand-inline{color:var(--red);font-weight:700;font-size:10.5px;line-height:12px;text-transform:uppercase;width:100px}
.rule{height:1px;background:var(--grey-line)}
.about-copy{left:121px;top:644px;width:253px;font-size:10.6px;line-height:14.8px;letter-spacing:.2px;text-align:justify}
.about-photo{left:391px;top:646px;width:171px;height:132px;border:1px solid var(--red);border-radius:4px;background:linear-gradient(135deg,#c9b8a4,#d8d3cc 50%,#9c8f84)}

/* services */
.services{left:602px;top:561px;width:223px}
.services header{height:34px;background:var(--blue);color:var(--white);display:flex;align-items:center;justify-content:space-between;padding:0 14px}
.services h2{font-size:19px;font-weight:500}
.services ul{list-style:none;background:var(--grey)}
.services li{height:26.2px;line-height:26px;padding-left:16px;font-size:10.6px;font-weight:500;color:var(--white);border-bottom:1px solid #dcdcdc}
.services li.current{background:var(--orange)}

/* testimonial */
.section-title{font-size:20px;font-style:italic;font-weight:700;color:var(--blue)}
.avatar{left:119px;top:860px;width:76px;height:76px;border-radius:50%;border:3px solid var(--blue);background:linear-gradient(160deg,#6fa6cf,#3d6f95)}
.quote{left:214px;top:862px;width:350px;font-size:10.6px;line-height:16px;letter-spacing:.2px}
.quote-author{left:214px;top:920px;font-size:11.5px;font-weight:500;color:var(--red)}

/* video */
.video{left:606px;top:804px;width:219px;height:136px;background:linear-gradient(135deg,#3b3b3b,#8a7d70 55%,#2c2c2c);border:2px solid #2b2b2b;box-shadow:0 6px 6px -3px rgba(0,0,0,.35)}
.video .bar{position:absolute;left:0;bottom:0;width:100%;height:18px;background:rgba(0,0,0,.75);color:var(--white);font-size:7px;display:flex;align-items:center;gap:6px;padding:0 6px}
.video .track{flex:1;height:3px;background:#555;border-radius:2px}
.video .play{position:absolute;left:50%;top:50%;width:24px;height:24px;margin:-18px 0 0 -12px;border-radius:50%;background:rgba(255,255,255,.45)}

/* promo */
.promo{left:118px;top:998px;width:444px;height:38px;background:var(--red);color:var(--white);font-size:21px;font-style:italic;font-weight:700;line-height:38px;padding-left:18px}
.badge{left:602px;top:965px;width:222px;height:80px;border:2px solid var(--blue-dark);border-radius:8px;background:linear-gradient(90deg,var(--white) 0 36%,var(--blue-dark) 36% 100%)}

/* estimate */
.estimate{left:0;top:1082px;width:944px;height:54px;background:repeating-linear-gradient(45deg,#ececec 0 2px,#f6f6f6 2px 5px)}
.estimate-label{left:0;top:1082px;width:262px;height:54px}
.estimate-label p{position:absolute;left:118px;top:10px;color:var(--white);font-weight:700;font-size:14px;line-height:17px}
.field{height:29px;background:var(--white);border:1px solid #d4d4d4;font-size:11px;padding-left:7px;line-height:27px;color:#444}
.submit{left:765px;top:1094px;width:60px;height:29px;background:var(--blue);color:var(--white);font-size:11px;font-weight:700;line-height:29px;text-align:center}

/* footer */
.footer{left:0;top:1136px;width:944px;height:64px;background:linear-gradient(180deg,var(--orange),var(--orange-light))}
.footer-links{left:120px;top:1149px;font-size:10px;font-weight:500;color:#3a2a10}
.copyright{left:120px;top:1174px;font-size:10px;font-weight:500;color:#3a2a10}
</style>
</head>
<body>

<!-- Header -->
<div class="abs brand"><span class="dot"></span>Dorvan Pipe<br>&amp; Boiler Inc.</div>
<div class="abs emergency">24 Hour Emergency<br>Service <span class="num">760 555-0142</span></div>
<div class="abs follow" style="left:741px;top:27px">Follow Us</div>
<div class="abs social" style="left:741px;top:42px"><span></span><span></span><span></span></div>

<!-- Navigation -->
<div class="abs nav-lines"></div>
<nav class="abs nav">
  <span style="width:97px"></span>
  <a class="active" href="#" style="width:77px">Home</a>
  <a href="#" style="width:93px">About Us</a>
  <a href="#" style="width:89px">Services</a>
  <a href="#" style="width:96px">Contact Us</a>
</nav>
<div class="abs nav-call">
  <svg width="18" height="18" viewBox="0 0 24 24"><path fill="#fff" d="M6.6 10.8a15.1 15.1 0 0 0 6.6 6.6l2.2-2.2c.3-.3.7-.4 1-.2 1.1.4 2.3.6 3.6.6.6 0 1 .4 1 1V20c0 .6-.4 1-1 1A17 17 0 0 1 3 4c0-.6.4-1 1-1h3.5c.6 0 1 .4 1 1 0 1.3.2 2.5.6 3.6.1.3 0 .7-.2 1z"/></svg>
</div>
<div class="abs nav-number">1-760-555-0187</div>

<!-- Hero -->
<div class="abs hero" role="img" aria-label="Photo of a smiling technician in a hard hat giving a thumbs up beside an outdoor AC unit"></div>
<div class="abs tagline">Providing quality work at affordable prices</div>

<!-- Welcome -->
<div class="abs welcome-title">
  <h1>Welcome To</h1>
  <span class="brand-inline">Dorvan Pipe<br>&amp; Boiler Inc.</span>
</div>
<div class="abs rule" style="left:120px;top:638px;width:442px"></div>
<p class="abs about-copy">We are a family owned and operated company providing plumbing, Heating and Air conditioning Services from central San Diego to North County. We have experts’ technicians to provide top-quality repair and installation for both residential and commercial clients. We now have fully equipped service trucks with the latest technology tools ready to respond to your emergency – any time of day or night.</p>
<div class="abs about-photo" role="img" aria-label="Photo of a hand tightening a sink drain pipe with a red wrench"></div>

<!-- Services -->
<section class="abs services">
  <header>
    <h2>Our Services</h2>
    <svg width="40" height="14" viewBox="0 0 40 14"><path d="M9 1 3 7l6 6M31 1l6 6-6 6" stroke="#d8e8f5" stroke-width="3" fill="none"/></svg>
  </header>
  <ul>
    <li class="current">• Water Heater Repair &amp; Installation</li>
    <li>• Boiler Repair &amp; Installation</li>
    <li>• Bathroom renovation</li>
    <li>• Kitchen Renovation</li>
    <li>• Water meters</li>
    <li>• Gas Meters</li>
    <li>• Slab Leaks find and Repair</li>
  </ul>
</section>

<!-- Testimonial -->
<h2 class="abs section-title" style="left:152px;top:810px">Our Customer Speaks About Us</h2>
<div class="abs rule" style="left:120px;top:846px;width:442px"></div>
<div class="abs avatar" role="img" aria-label="Customer portrait photo"></div>
<p class="abs quote">Per suscipit lobortis nisl ut aliquip ex ea commodo consequat. Duis autem vl eum iriure dolor in hendrerit in vulputate velit esse molestie consequat, veler illum dolore eu feugiat nulla facilisis at vero eros et .</p>
<div class="abs quote-author">- Mr Abc, LOREM IPSUM</div>

<!-- Video -->
<div class="abs video" role="img" aria-label="Video still of a technician testing gas pressure with a manometer">
  <span class="play"></span>
  <div class="bar">
    <svg width="7" height="8" viewBox="0 0 7 8"><path d="M0 0l7 4-7 4z" fill="#fff"/></svg>
    <span>04:59</span><span class="track"></span><span>10:35</span>
  </div>
</div>

<!-- Promo & accreditation -->
<div class="abs promo">Save Up To 20% On New Installation..</div>
<div class="abs badge" role="img" aria-label="KTW accredited business badge"></div>

<!-- Estimate form -->
<div class="abs estimate"></div>
<div class="abs estimate-label">
  <svg width="262" height="54" viewBox="0 0 262 54"><defs><linearGradient id="eg" x1="0" x2="0" y1="0" y2="1"><stop offset="0" stop-color="#1a8ad6"/><stop offset="1" stop-color="#075ea3"/></linearGradient></defs><path d="M0 0h240l22 27-22 27H0z" fill="url(#eg)"/></svg>
  <p>REQUEST A FREE<br>ESTIMATE TODAY!</p>
</div>
<div class="abs field" style="left:266px;top:1094px;width:175px">Name</div>
<div class="abs field" style="left:453px;top:1094px;width:142px">Phone</div>
<div class="abs field" style="left:608px;top:1094px;width:142px">Email</div>
<div class="abs submit">SUBMIT</div>

<!-- Footer -->
<footer class="abs footer"></footer>
<div class="abs footer-links">Home &nbsp;|&nbsp; About Us &nbsp;|&nbsp; Services &nbsp;|&nbsp; Contact Us</div>
<div class="abs copyright">© 2014 Dorvan Pipe &amp; Boiler Inc.all Rights Reserved.</div>
<div class="abs follow" style="left:741px;top:1150px;color:#3a2a10">Follow Us</div>
<div class="abs social" style="left:741px;top:1166px"><span></span><span></span><span></span></div>

</body>
</html>
```